Monthly Planner & To Do List on dry erase magnetic whiteboard

I'm after 2 x designs for magnetic whiteboards.
1. 17 x 13 inches is a monthly planner. Dates and month can be written in each month and then wiped off and re-written for the next month.
2. 6 x 4 inches - to do list however I don't want this to say To Do on it but will have lines to write on and possibly bullet points to check off.
I have attached below samples of other products (the ones I like the most are the first two - 9.19.52 and 9.20.34). I actually don't like the design of the others but just show them here as an example for layout purposes.
I want something that is modern, slick, simple yet stylish which is what my brand is representative of - smart, modern, organised. It will be printed onto a white board and I only want the print to be in black, no grey shading. I need a more modern font and don't like any of the swirly parts. Just clean and simple but slick.
I would like the size of the day squares to be as large as possible to fit writing in them and also for a section somewhere on the page for additional notes.

• Old style fonts, cartoon style or childish.

```html
<!DOCTYPE html>
<html lang="en">
<head>
<meta charset="UTF-8">
<title>Monthly Planner</title>
<link rel="stylesheet" href="https://fonts.googleapis.com/css2?family=Tenor+Sans&display=swap">
<style>
  :root {
    --ink: #000000;
    --board: #ffffff;
    --frame: #8a8a8a;
    --line: 1px;
  }
  * { box-sizing: border-box; margin: 0; padding: 0; }
  html, body {
    width: 1200px;
    height: 918px;
    overflow: hidden;
    background: var(--board);
  }
  .planner {
    position: relative;
    width: 1200px;
    height: 918px;
    background: var(--board);
    font-family: "Tenor Sans", sans-serif;
    color: var(--ink);
  }
  .board-edge {
    position: absolute;
    inset: 1px;
    border: 1px solid var(--frame);
    border-radius: 12px;
  }
  .month-grid {
    position: absolute;
    left: 28px;
    top: 18px;
    width: 927px;
    height: 882px;
    border-top: var(--line) solid var(--ink);
    border-left: var(--line) solid var(--ink);
    display: grid;
    grid-template-columns: repeat(7, 1fr);
    grid-template-rows: repeat(5, 1fr);
  }
  .day-cell {
    position: relative;
    border-right: var(--line) solid var(--ink);
    border-bottom: var(--line) solid var(--ink);
  }
  .day-name {
    position: absolute;
    left: 13px;
    top: 12px;
    font-size: 19px;
    line-height: 1;
    font-weight: 400;
    letter-spacing: 0.2px;
  }
  .date-field {
    position: absolute;
    left: 966px;
    top: 18px;
    width: 224px;
    height: 33px;
    border-top: var(--line) solid var(--ink);
    border-left: var(--line) solid var(--ink);
    border-bottom: var(--line) solid var(--ink);
    border-top-left-radius: 8px;
  }
  .date-slash {
    position: absolute;
    left: 131px;
    top: 3px;
    font-size: 24px;
    line-height: 1;
  }
  .memo-panel {
    position: absolute;
    left: 966px;
    top: 62px;
    width: 224px;
    height: 838px;
    border-top: var(--line) solid var(--ink);
    border-left: var(--line) solid var(--ink);
    border-top-left-radius: 8px;
    border-top-right-radius: 4px;
  }
  .memo-title {
    position: absolute;
    left: 0;
    right: 0;
    top: 12px;
    text-align: center;
    font-size: 21px;
    font-weight: 400;
    line-height: 1;
    text-decoration: underline;
    text-underline-offset: 3px;
    text-decoration-thickness: 1px;
  }
</style>
</head>
<body>
<main class="planner">
  <div class="board-edge"></div>

  <section class="month-grid">
    <div class="day-cell"><span class="day-name">SUN</span></div>
    <div class="day-cell"><span class="day-name">MON</span></div>
    <div class="day-cell"><span class="day-name">TUES</span></div>
    <div class="day-cell"><span class="day-name">WED</span></div>
    <div class="day-cell"><span class="day-name">THU</span></div>
    <div class="day-cell"><span class="day-name">FRI</span></div>
    <div class="day-cell"><span class="day-name">SAT</span></div>

    <div class="day-cell"></div><div class="day-cell"></div><div class="day-cell"></div><div class="day-cell"></div><div class="day-cell"></div><div class="day-cell"></div><div class="day-cell"></div>
    <div class="day-cell"></div><div class="day-cell"></div><div class="day-cell"></div><div class="day-cell"></div><div class="day-cell"></div><div class="day-cell"></div><div class="day-cell"></div>
    <div class="day-cell"></div><div class="day-cell"></div><div class="day-cell"></div><div class="day-cell"></div><div class="day-cell"></div><div class="day-cell"></div><div class="day-cell"></div>
    <div class="day-cell"></div><div class="day-cell"></div><div class="day-cell"></div><div class="day-cell"></div><div class="day-cell"></div><div class="day-cell"></div><div class="day-cell"></div>
  </section>

  <div class="date-field"><span class="date-slash">/</span></div>

  <aside class="memo-panel">
    <h2 class="memo-title">Memo</h2>
  </aside>
</main>
</body>
</html>
```